Brightpath Letterhead

We would like a letterhead for our company. I have uploaded our logo.

Brightpath Ridge Consulting
1450 W Corliss Ave Ste 310
Arlington, TX 76006
833-517-2906

```html
<!DOCTYPE html>
<html lang="en">
<head>
<meta charset="utf-8">
<title>Brightpath Ridge Consulting – Letterhead</title>
<link rel="stylesheet" href="https://fonts.googleapis.com/css2?family=Open+Sans:wght@400;700&display=swap">
<style>
  :root {
    --paper: #f4f4f4;
    --teal: #065f6b;
    --mint: #6cc49a;
    --ink: #1c1c1c;
    --light: #f4f4f4;
  }
  * { margin: 0; padding: 0; box-sizing: border-box; }
  html, body { width: 848px; height: 1200px; overflow: hidden; background: var(--paper); }
  body { font-family: "Open Sans", Arial, sans-serif; color: var(--ink); }
  .letterhead { position: relative; width: 848px; height: 1200px; overflow: hidden; background: var(--paper); }

  .top-band { position: absolute; left: 242px; top: 0; right: 0; height: 49px; background: var(--mint); }
  .corner-decor {
    position: absolute; left: 0; top: 0; width: 228px; height: 240px;
    background: linear-gradient(135deg, var(--teal) 0%, var(--teal) 35%, var(--mint) 75%, var(--paper) 100%);
    opacity: 0.85;
  }

  .brand { position: absolute; right: 54px; top: 119px; display: flex; align-items: center; gap: 12px; }
  .brand-dot { width: 22px; height: 22px; border-radius: 50%; background: var(--teal); flex: none; }
  .brand-name { font-weight: 700; font-size: 21px; letter-spacing: 2px; text-transform: uppercase; color: var(--teal); white-space: nowrap; }

  .recipient { position: absolute; left: 127px; top: 286px; font-size: 17.1px; line-height: 20.5px; }
  .dateline { position: absolute; right: 134px; top: 285px; font-size: 17.1px; line-height: 20.5px; text-align: right; }

  .salutation { position: absolute; left: 127px; top: 422px; font-size: 16px; }
  .body-text { position: absolute; left: 127px; width: 594px; font-size: 17.6px; line-height: 18.8px; text-align: justify; hyphens: auto; -webkit-hyphens: auto; }
  .body-text.p1 { top: 486px; }
  .body-text.p2 { top: 570px; }
  .body-text.p3 { top: 689px; }

  .signoff { position: absolute; right: 131px; top: 898px; font-size: 16px; line-height: 20.5px; text-align: right; }
  .signoff .signer { margin-top: 20px; }

  .footer { position: absolute; left: 0; top: 1054px; width: 848px; height: 146px; background: var(--teal); color: var(--light); overflow: hidden; }
  .footer-name { position: absolute; left: 37px; top: 29px; font-weight: 700; font-size: 18px; line-height: 24px; }
  .contact { position: absolute; left: 37px; display: flex; align-items: center; gap: 12px; font-size: 17.5px; line-height: 24px; }
  .contact.address { top: 64px; }
  .contact.phone { top: 93px; }
  .contact svg { width: 15px; height: 15px; flex: none; }
  .footer-decor {
    position: absolute; left: 563px; top: 0; width: 285px; height: 146px;
    background: linear-gradient(120deg, var(--teal) 0%, #4f8f93 55%, var(--light) 100%);
    opacity: 0.6;
  }
</style>
</head>
<body>
<main class="letterhead">
  <div class="corner-decor" role="img" aria-label="Decorative corner graphic in teal and mint"></div>
  <div class="top-band"></div>

  <div class="brand">
    <span class="brand-dot"></span>
    <span class="brand-name">Brightpath Ridge Consulting</span>
  </div>

  <section class="recipient">
    <p>To:</p>
    <p>Name of Person</p>
    <p>Post/Designation</p>
  </section>
  <section class="dateline">
    <p>Date:</p>
    <p>21-07-2022</p>
  </section>

  <p class="salutation">Dear,</p>

  <p class="body-text p1">Lorem ipsum dolor sit amet, consectetur adipiscing elit. Donec fringilla neque euismod volutpat cursus. Vestibulum ac pretium orci, consequat elementum velit. Etiam bibendum purus ac augue finibus volutpat. Vestibulum justo nisl</p>
  <p class="body-text p2">Lorem ipsum dolor sit amet, consectetur adipiscing elit. Donec fringilla neque euismod volutpat cursus. Vestibulum ac pretium orci, consequat elementum velit. Etiam bibendum purus ac augue finibus volutpat. Vestibulum justo nisl, gravida aliquet sollicitudin ut, finibus vitae mi. Praesent aliquet scelerisque blandit. sapien, ac porttitor mauris tristique nec.</p>
  <p class="body-text p3">Lorem ipsum dolor sit amet, consectetur adipiscing elit. Donec fringilla neque euismod volutpat cursus. Vestibulum ac pretium orci, consequat elementum velit. Etiam bibendum purus ac augue finibus volutpat. Vestibulum justo nisl, gravida aliquet sollicitudin ut, finibus vitae mi. Praesent aliquet scelerisque blandit. Sed id varius lacus, id tristique sem. Fusce et lobortis leo. Aliquam mollis pellentesque magna, condimentum ullamcorper ex ullamcorper non. Morbi ultricies nunc eu tellus dignissim, eget venenatis dolor ullamcorper. Etiam dolor eros, iaculis at ultricies nec, volutpat nec orci. Vivamus tincidunt rutrum sapien, ac porttitor mauris tristique nec.</p>

  <section class="signoff">
    <p>Regard</p>
    <div class="signer">
      <p>John Doe</p>
      <p>Director</p>
    </div>
  </section>

  <footer class="footer">
    <div class="footer-decor" role="img" aria-label="Decorative footer graphic in teal and light grey"></div>
    <p class="footer-name">Brightpath Ridge Consulting</p>
    <p class="contact address">
      <svg viewBox="0 0 24 24" aria-hidden="true"><path d="M12 2a7 7 0 0 0-7 7c0 5 7 13 7 13s7-8 7-13a7 7 0 0 0-7-7zm0 9.5A2.5 2.5 0 1 1 12 6.5a2.5 2.5 0 0 1 0 5z" fill="var(--mint)"/></svg>
      <span>1450 W Corliss Ave Ste 310, Arlington, TX 76006</span>
    </p>
    <p class="contact phone">
      <svg viewBox="0 0 24 24" aria-hidden="true"><path d="M6.6 10.8a15.1 15.1 0 0 0 6.6 6.6l2.2-2.2a1 1 0 0 1 1-.25 11.4 11.4 0 0 0 3.6.57 1 1 0 0 1 1 1V20a1 1 0 0 1-1 1A17 17 0 0 1 3 4a1 1 0 0 1 1-1h3.5a1 1 0 0 1 1 1c0 1.25.2 2.45.57 3.570a1 1 0 0 1-.25 1z" fill="var(--mint)"/></svg>
      <span>833-517-2906</span>
    </p>
  </footer>
</main>
</body>
</html>
```